Pale Ridge Software

We are a software company selling endpoint visibility, access and security technology to enterprise-level IT departments.

Our technology helps organizations gain comprehensive visibility into and control over devices accessing their corporate network so they can quickly identify and address suspicious activity on the network that could lead to potential threats like data breaches.

This technology can cost organizations upwards of $1M - depending on the size of the organization. Our primary clients are Summit 3,000 companies.

We want a professional, polished business card to represent our new brand.

Info fields to include on the card:
Name
Job Title
Office Phone #
Cell Phone #
Email address
Address: 4172 Wexmoor Pond Ave., Ste. 2600, Bloomington, MN 55819
Website address: www.paleridgesoftware.example
Tagline: See every device. Secure the network.

Logo files and color specs document are attached. Would like color scheme to coordinate with the logo.

Also looking at stationary/envelope designs in conjunction with the business card designs. Received very few designs that included the stationary.

```html
<!DOCTYPE html>
<html lang="en">
<head>
<meta charset="utf-8">
<title>Pale Ridge Software — Business Card</title>
<link rel="stylesheet" href="https://fonts.googleapis.com/css2?family=Open+Sans:wght@300;400;600;700&display=swap">
<style>
  :root {
    --brand-red: #b3303a;
    --brand-red-dark: #8f1f28;
    --fold-grey: #d9d9d9;
    --ink: #2b2b2b;
    --ink-soft: #555;
    --paper: #ffffff;
    --backdrop: #eceae7;
  }
  * { box-sizing: border-box; margin: 0; padding: 0; }
  html, body { width: 1200px; height: 800px; overflow: hidden; }
  body {
    background: var(--backdrop);
    font-family: "Open Sans", Arial, sans-serif;
    position: relative;
  }

  /* Back of card */
  .card-back {
    position: absolute;
    left: 110px; top: 120px;
    width: 320px; height: 560px;
    background: linear-gradient(135deg, #c13a44 0%, var(--brand-red) 45%, var(--brand-red-dark) 100%);
    box-shadow: 0 6px 18px rgba(0,0,0,.18);
  }
  .card-back .tagline {
    position: absolute;
    left: 58px; top: 40px;
    transform-origin: left top;
    transform: translateX(24px) rotate(90deg);
    white-space: nowrap;
    color: #fff;
    font-weight: 300;
    font-size: 21px;
    letter-spacing: .3px;
  }
  .card-back .wordmark {
    position: absolute;
    left: 50%; top: 50%;
    transform: translate(-50%, -50%) rotate(90deg);
    white-space: nowrap;
    color: #fff;
    font-weight: 600;
    font-size: 18px;
    letter-spacing: 4px;
    text-transform: uppercase;
  }

  /* Front of card */
  .card-front {
    position: absolute;
    left: 480px; top: 220px;
    width: 640px; height: 366px;
    background: var(--paper);
    box-shadow: 0 6px 18px rgba(0,0,0,.18);
  }
  .ribbon {
    position: absolute;
    left: 190px; top: 0;
    width: 330px; height: 110px;
  }
  .holder {
    position: absolute;
    left: 230px; top: 14px;
    color: #fff;
  }
  .holder .name {
    font-weight: 600;
    font-size: 19px;
    letter-spacing: 1px;
    text-transform: uppercase;
  }
  .holder .title {
    font-size: 11px;
    letter-spacing: 1px;
    text-transform: uppercase;
    margin-top: 2px;
    padding-left: 8px;
  }
  .company-name {
    position: absolute;
    right: 34px; top: 118px;
    text-align: right;
    color: var(--brand-red-dark);
    font-weight: 600;
    text-transform: uppercase;
    line-height: 1.1;
  }
  .company-name .primary {
    display: block;
    font-size: 26px;
    letter-spacing: 3px;
  }
  .company-name .secondary {
    display: block;
    font-size: 16px;
    letter-spacing: 9px;
    margin-right: -9px;
  }

  .contacts {
    position: absolute;
    left: 36px; top: 120px;
    list-style: none;
  }
  .contacts li {
    display: flex;
    align-items: center;
    gap: 10px;
    font-size: 14px;
    color: var(--ink-soft);
    line-height: 24px;
  }
  .contacts svg { width: 14px; height: 14px; flex: none; }

  .address {
    position: absolute;
    right: 34px; bottom: 34px;
    text-align: right;
    font-size: 15px;
    line-height: 22px;
    color: var(--ink);
    font-style: normal;
  }
  .address .web {
    color: var(--brand-red);
    font-weight: 700;
  }
</style>
</head>
<body>

  <section class="card-back" aria-label="Card back">
    <p class="tagline">See every device. Secure the network.</p>
    <p class="wordmark">Pale Ridge Software</p>
  </section>

  <section class="card-front" aria-label="Card front">
    <svg class="ribbon" viewBox="0 0 330 110" aria-hidden="true">
      <polygon points="0,0 270,0 330,70 0,70" fill="var(--brand-red)"/>
      <polygon points="270,70 330,70 330,108" fill="var(--fold-grey)"/>
    </svg>
    <div class="holder">
      <p class="name">Evan Marlow</p>
      <p class="title">Director</p>
    </div>

    <p class="company-name"><span class="primary">Pale Ridge</span><span class="secondary">Software</span></p>

    <ul class="contacts">
      <li>
        <svg viewBox="0 0 14 14" aria-hidden="true"><circle cx="7" cy="7" r="7" fill="var(--brand-red)"/><path d="M4.5 3.6c.4-.3.8-.2 1 .2l.6 1.1c.2.4 0 .7-.3.9l-.3.2c.3.8.9 1.5 1.7 1.9l.3-.3c.3-.3.6-.4.9-.2l1.1.7c.4.2.4.7.1 1l-.5.5c-2.6.4-5.6-2.8-5-5.4z" fill="#fff"/></svg>
        218-555-0147
      </li>
      <li>
        <svg viewBox="0 0 14 14" aria-hidden="true"><circle cx="7" cy="7" r="7" fill="var(--brand-red)"/><rect x="5" y="3.2" width="4" height="7.6" rx=".8" fill="#fff"/><rect x="5.7" y="4.2" width="2.6" height="4.6" fill="var(--brand-red)"/></svg>
        218-555-0192
      </li>
      <li>
        <svg viewBox="0 0 14 14" aria-hidden="true"><circle cx="7" cy="7" r="7" fill="var(--brand-red)"/><rect x="3.6" y="4.6" width="6.8" height="4.8" fill="#fff"/><path d="M3.6 4.6 7 7.4l3.4-2.8" fill="none" stroke="var(--brand-red)" stroke-width=".8"/></svg>
        emarlow@paleridgesoftware.example
      </li>
    </ul>

    <address class="address">
      4172 Wexmoor Pond Ave.<br>
      Ste. 2600, Bloomington, MN 55819<br>
      <span class="web">www.paleridgesoftware.example</span>
    </address>
  </section>

</body>
</html>
```